Template Design auf Basis der Brenvik Suite 3
Zielgruppe
3 Internet Communitys zum Thema Fahrrad, Roller und Motorrad
Es wird auf den Plattformen jeweils ein großer Diskussionsforum geben (primäre Funktion) aber auch weitere Funktionen wie zum Beispiel eine Fotogalerie, Marktplatz und Userkarte.
Aufgabenstellung
Es geht um die Gestaltung der Benutzeroberfläche von 3 Internet Foren rund um Fahrrad, Motor-Roller und Motorräder auf Basis der Brenvik Suite 3. Somit Template Design.
https://www.brenvik-forum.example/de/
Die Designs sollen quasi identisch sein nur Logo, Farbgestaltung und Grafiken sich unterscheiden. Die Zusammengehörigkeit muss klar ersichtlich sein. Logos stehen bereits fest und sind hier angehängt.
Das Design soll frisch und modern sein, aber diverse Altersgruppen ansprechen und intuitiv bedienbar sein. Menüs müssen leicht zu finden und zu bedienen sein.
Alle Seiten müssen Responsive Design beinhalten und hochauflösende Grafiken für z.B. Lumora Displays unterstützen.
Designer die ein entsprechendes Template umsetzen können, bitte einen entsprechenden Hinweis zum Entwurf dazu schreiben. Ein entsprechender Auftrag soll auch vergeben werden.

```html
<!DOCTYPE html>
<html lang="de">
<head>
<meta charset="utf-8">
<title>Roller.Treff – Forum</title>
<link href="https://fonts.googleapis.com/css2?family=Raleway:ital,wght@0,400;0,500;0,600;0,700;1,400;1,500&display=swap" rel="stylesheet">
<style>
:root{
  --dark:#333331;
  --blue:#2a8be0;
  --panel:#e6e6e8;
  --field:#c8c4c4;
  --text:#444;
  --muted:#777;
  --green:#a6d21b;
  --red:#f0451f;
  --white:#fff;
}
*{box-sizing:border-box;margin:0;padding:0}
html,body{width:1200px;height:2348px;overflow:hidden;background:var(--white)}
body{font-family:'Raleway',sans-serif;color:var(--text);position:relative}
.abs{position:absolute}
a{color:inherit;text-decoration:none}

.topbar{left:0;top:0;width:1200px;height:36px;background:var(--dark);color:#eee;font-size:15px}
.topbar .phone{left:48px;top:8px;display:flex;align-items:center;gap:6px}
.topbar .account{left:705px;top:10px;font-size:14px;display:flex;gap:6px;align-items:center}
.topbar .lang{left:928px;top:9px;font-size:14px;display:flex;gap:5px;align-items:center}
.topbar .social{left:1043px;top:8px;display:flex;gap:8px}
.topbar .social span{width:19px;height:19px;border:1.5px solid #eee;border-radius:50%;display:block}

.header{left:0;top:36px;width:1200px;height:71px;background:var(--white)}
.brand{display:flex;align-items:center;gap:8px;font-weight:700;font-size:20px;color:var(--blue)}
.brand i{width:22px;height:22px;border-radius:50%;background:var(--blue);display:block}
.header .brand{left:44px;top:24px}
.mainnav{right:82px;top:25px;display:flex;gap:12px;font-size:18px;color:#555;letter-spacing:.3px}
.mainnav .active{color:var(--blue);font-weight:600}

.hero{left:0;top:107px;width:1200px;height:216px;background:linear-gradient(90deg,#8a8d8e,#c9c6c0 40%,#6f7072 60%,#aaa9a4)}
.hero h1{position:absolute;left:0;right:0;top:70px;text-align:center;color:#fff;font-size:29px;font-weight:700;line-height:36px;text-shadow:0 1px 3px rgba(0,0,0,.35)}

.subbar{left:0;top:323px;width:1200px;height:49px;background:var(--blue)}
.search{left:51px;top:12px;width:406px;height:27px;background:#fff;display:flex}
.search span{flex:1;font-style:italic;font-size:13px;padding:6px 16px;color:#444}
.search b{width:27px;background:var(--dark);display:flex;align-items:center;justify-content:center}
.communities{right:92px;top:15px;color:#fff;font-size:15px;display:flex;gap:8px}

.section-title{left:0;width:1200px;text-align:center;font-weight:700;color:var(--dark);font-size:28px}
.rule{height:3px;background:#bbb;width:120px;left:540px}
.lead{left:0;width:1200px;text-align:center;font-style:italic;font-weight:500;font-size:15px;line-height:19px;color:#222}

.panel-head{background:var(--dark);color:#fff;font-size:19px;font-weight:700;border-left:7px solid var(--blue);display:flex;align-items:center;gap:10px;padding-left:15px}
.panel-head .chev{margin-left:auto;margin-right:16px}
.cat{font-size:16px;color:#555;padding:20px 0 8px 11px;border-bottom:3px solid #ccc;width:697px}
.row{position:relative;height:65px}
.row .ico{position:absolute;left:10px;top:4px}
.row .t{position:absolute;left:55px;top:0;color:var(--blue);font-size:16px}
.row .d{position:absolute;left:55px;top:21px;font-size:12px;line-height:14px;color:#555;width:330px}
.row .s{position:absolute;left:420px;top:21px;font-size:12px;line-height:14px;color:#555}
.row .av{position:absolute;left:555px;top:10px}
.row .n{position:absolute;left:595px;top:9px;font-size:15px;color:#333}
.row .m{position:absolute;left:595px;top:28px;font-size:11px;color:#555}

.side{background:var(--panel)}
.side .panel-head{height:43px;padding-left:22px}
.item{display:flex;gap:8px;align-items:flex-start;padding:0 10px;margin-top:14px}
.item .av{width:32px;height:32px;border-radius:50%;flex:none}
.item .t{color:var(--blue);font-size:15px;line-height:17px}
.item .m{font-size:11px;color:#444}
.photo{background:radial-gradient(circle,#3b7fc2,#4b5d3c)}
.blank{background:#d7d7d7}
.login label{display:block;font-size:10px;color:#444;margin:8px 0 3px 16px}
.login .f{margin-left:16px;width:283px;height:23px;background:var(--field)}
.login .btn{position:absolute;right:20px;bottom:13px;background:var(--blue);color:#fff;font-size:12px;font-weight:700;border-radius:12px;padding:5px 21px}
.login .forgot{position:absolute;left:16px;bottom:19px;font-size:8px;font-style:italic;line-height:10px}

.totop{left:1139px;top:1301px;width:61px;height:62px;background:var(--dark);display:flex;align-items:center;justify-content:center}

.card{top:1646px;width:322px;height:222px}
.card .img{width:100%;height:173px}
.card .arc{position:absolute;left:0;top:122px;width:150px;height:100px;background:#fff;border-radius:80px 80px 0 0}
.card .brand{position:absolute;left:6px;top:172px;font-size:17px}
.card .cta{position:absolute;right:0;top:182px;color:#fff;font-weight:700;font-size:16px;padding:9px 15px;border-radius:20px}

.map{left:0;top:1940px;width:1200px;height:146px;background:linear-gradient(180deg,#e0e0e0,#c9c9c9)}
.footer{left:0;top:2086px;width:1200px;height:223px;background:var(--dark);color:#999}
.footer .brand{position:absolute;left:50px;top:35px;font-size:21px}
.footer .about{position:absolute;left:52px;top:92px;width:310px;font-size:11.5px;line-height:15px}
.fcol{position:absolute;top:42px}
.fcol h3{color:var(--blue);font-weight:500;font-size:16px;padding-bottom:6px;border-bottom:1px solid #888;width:198px}
.fcol ul{list-style:none;font-size:11.5px;line-height:15px;margin-top:12px}
.fpost{display:flex;gap:7px;margin-top:12px;color:#eee;font-size:14px}
.fpost i{width:31px;height:31px;border-radius:50%;background:#ddd;flex:none}
.fpost small{display:block;color:#888;font-size:10px}
.nl input{display:block;margin-top:16px;width:198px;height:24px;border:none;font:12px 'Raleway',sans-serif;padding-left:8px}
.nl .go{margin-top:8px;width:198px;height:20px;background:var(--blue);color:#fff;font-size:11px;text-align:center;line-height:20px}
.bottombar{left:0;top:2309px;width:1200px;height:39px;background:#222;color:#ddd;font-size:11px;text-align:center;line-height:39px}
</style>
</head>
<body>

<svg width="0" height="0" style="position:absolute">
  <defs>
    <symbol id="user" viewBox="0 0 34 34"><circle cx="17" cy="17" r="17" fill="#2a8be0"/><circle cx="17" cy="13" r="5" fill="#fff"/><path d="M8 25a9 7 0 0 1 18 0z" fill="#fff"/></symbol>
    <symbol id="chat" viewBox="0 0 40 32"><ellipse cx="17" cy="12" rx="15" ry="10" fill="#333"/><path d="M7 19l-3 7 9-5z" fill="#333"/><path d="M24 24c8 1 14-3 14-8" stroke="#333" stroke-width="2.5" fill="none"/><path d="M32 22l4 6-8-3" fill="#333"/></symbol>
    <symbol id="chev" viewBox="0 0 20 12"><path d="M2 2l8 8 8-8" stroke="#2a8be0" stroke-width="3.5" fill="none"/></symbol>
  </defs>
</svg>

<div class="abs topbar">
  <div class="abs phone"><svg width="10" height="15" viewBox="0 0 10 15"><rect x="1" y="1" width="8" height="13" rx="1.5" fill="none" stroke="#eee" stroke-width="1.6"/></svg>Für Fragen rufen Sie uns an: 09876 / 543210</div>
  <div class="abs account"><svg width="12" height="13" viewBox="0 0 12 13"><circle cx="6" cy="4" r="3.2" fill="#2a8be0"/><path d="M0 13a6 5 0 0 1 12 0z" fill="#2a8be0"/></svg>Anmelden oder Registrieren</div>
  <div class="abs lang"><svg width="14" height="14"><circle cx="7" cy="7" r="7" fill="#c33"/><rect x="0" y="5.5" width="14" height="3" fill="#fff"/></svg>ENGLISH <svg width="14" height="11"><rect width="14" height="11" fill="#ccc"/><path d="M3 3l4 5 4-5z" fill="#333"/></svg></div>
  <div class="abs social"><span></span><span></span><span></span></div>
</div>

<div class="abs header">
  <div class="abs brand"><i></i>Roller.Treff</div>
  <nav class="abs mainnav"><a class="active">DASHBOARD</a>|<a>FORUM</a>|<a>MITGLIEDER</a>|<a>MARKTPLATZ</a>|<a>GALERIE</a>|<a>KALENDER</a></nav>
</div>

<div class="abs hero" role="img" aria-label="Foto: Rollerfahrerin in Bewegung, verwischter Hintergrund">
  <h1>WILLKOMMEN IN UNSERER<br>ROLLER.TREFF</h1>
</div>

<div class="abs subbar">
  <div class="abs search"><span>Jetzt die Suche starten</span><b><svg width="16" height="16" viewBox="0 0 16 16"><circle cx="6.5" cy="6.5" r="5" stroke="#fff" stroke-width="2.2" fill="none"/><path d="M10 10l5 5" stroke="#fff" stroke-width="2.5"/></svg></b></div>
  <div class="abs communities"><a>FAHRRAD-TREFF</a>|<a>MOTORRAD-TREFF</a>|<a>ROLLER-TREFF</a></div>
</div>

<h2 class="abs section-title" style="top:424px">FORUM / FAHRRAD.TREFF</h2>
<div class="abs rule" style="top:467px"></div>
<p class="abs lead" style="top:484px">Um losschreiben zu können müssen Sie angemeldet sein.<br>Entweder loggen Sie sich gleich ein oder registrieren Sie sich.</p>

<section class="abs" style="left:39px;top:564px;width:722px">
  <div class="panel-head" style="height:43px"><svg width="20" height="18" viewBox="0 0 20 18"><rect x="1" y="3" width="14" height="14" rx="2" stroke="#fff" stroke-width="1.8" fill="none"/><path d="M8 11l9-9 2 2-9 9H8z" fill="#fff"/></svg>ALLGEMEINE FRAGEN<svg class="chev" width="18" height="11"><use href="#chev"/></svg></div>
  <div class="cat">ERSTE KATEGORIE</div>
  <div style="padding-top:20px">
    <div class="row"><svg class="ico" width="40" height="32"><use href="#chat"/></svg><a class="t">Neuigkeiten über die Community</a><p class="d">Lorem ipsum dolor sit amet, consetetur sadipscing diam voluptua. Lorem ipsum dolor sit amet, consetetur.</p><p class="s">2 Themen<br>6 Beiträge</p><svg class="av" width="33" height="33"><use href="#user"/></svg><span class="n">Fahrradtour</span><span class="m">Paul · 20. April 2017</span></div>
    <div class="row"><svg class="ico" width="40" height="32"><use href="#chat"/></svg><a class="t">Neuigkeiten über die Community</a><p class="d">Lorem ipsum dolor sit amet, consetetur sadipscing diam voluptua. Lorem ipsum dolor sit amet, consetetur.</p><p class="s">2 Themen<br>6 Beiträge</p><svg class="av" width="33" height="33"><use href="#user"/></svg><span class="n">Fahrradtour</span><span class="m">Paul · 20. April 2017</span></div>
    <div class="row"><svg class="ico" width="40" height="32"><use href="#chat"/></svg><a class="t">Neuigkeiten über die Community</a><p class="d">Lorem ipsum dolor sit amet, consetetur sadipscing diam voluptua. Lorem ipsum dolor sit amet, consetetur.</p><p class="s">2 Themen<br>6 Beiträge</p><svg class="av" width="33" height="33"><use href="#user"/></svg><span class="n">Fahrradtour</span><span class="m">Paul · 20. April 2017</span></div>
  </div>
</section>

<section class="abs" style="left:37px;top:907px;width:722px">
  <div class="panel-head" style="height:43px"><svg width="22" height="18" viewBox="0 0 22 18"><ellipse cx="11" cy="8" rx="9.5" ry="6.5" stroke="#fff" stroke-width="1.8" fill="none"/><path d="M4 12l-2 5 6-3" stroke="#fff" stroke-width="1.8" fill="none"/></svg>SUPPORT<svg class="chev" width="18" height="11"><use href="#chev"/></svg></div>
  <div class="cat">ERSTE KATEGORIE</div>
  <div style="padding-top:20px">
    <div class="row"><svg class="ico" width="40" height="32"><use href="#chat"/></svg><a class="t">Neuigkeiten über die Community</a><p class="d">Lorem ipsum dolor sit amet, consetetur sadipscing diam voluptua. Lorem ipsum dolor sit amet, consetetur.</p><p class="s">2 Themen<br>6 Beiträge</p><svg class="av" width="33" height="33"><use href="#user"/></svg><span class="n">Fahrradtour</span><span class="m">Paul · 20. April 2017</span></div>
    <div class="row"><svg class="ico" width="40" height="32"><use href="#chat"/></svg><a class="t">Neuigkeiten über die Community</a><p class="d">Lorem ipsum dolor sit amet, consetetur sadipscing diam voluptua. Lorem ipsum dolor sit amet, consetetur.</p><p class="s">2 Themen<br>6 Beiträge</p><svg class="av" width="33" height="33"><use href="#user"/></svg><span class="n">Fahrradtour</span><span class="m">Paul · 20. April 2017</span></div>
    <div class="row"><svg class="ico" width="40" height="32"><use href="#chat"/></svg><a class="t">Neuigkeiten über die Community</a><p class="d">Lorem ipsum dolor sit amet, consetetur sadipscing diam voluptua. Lorem ipsum dolor sit amet, consetetur.</p><p class="s">2 Themen<br>6 Beiträge</p><svg class="av" width="33" height="33"><use href="#user"/></svg><span class="n">Fahrradtour</span><span class="m">Paul · 20. April 2017</span></div>
  </div>
</section>

<aside class="abs side login" style="left:793px;top:564px;width:317px;height:181px">
  <div class="panel-head">LOGIN</div>
  <label>Benutzername:</label><div class="f"></div>
  <label>Passwort:</label><div class="f"></div>
  <p class="forgot">Passwort vergessen?<br>Hier klicken</p>
  <span class="btn">EINLOGGEN</span>
</aside>

<aside class="abs side" style="left:792px;top:770px;width:317px;height:220px">
  <div class="panel-head">HEIßE THEMEN</div>
  <div class="item"><i class="av photo"></i><div><a class="t">Neues Communitydesign</a><p class="m">Anna · 27. April 2017</p></div></div>
  <div class="item"><i class="av photo"></i><div><a class="t">Fahrradstorys aus dem Süden</a><p class="m">Anna · 27. April 2017</p></div></div>
  <div class="item"><svg class="av" width="32" height="32"><use href="#user"/></svg><div><a class="t">Die peinlichsten Ausflüge</a><p class="m">Paul · 20. April 2017</p></div></div>
</aside>

<aside class="abs side" style="left:793px;top:1018px;width:317px;height:248px">
  <div class="panel-head">LETZTE BEITRÄGE</div>
  <div class="item"><i class="av photo"></i><div><a class="t">Willkommen als Admin</a><p class="m">Anna · 27. April 2017</p></div></div>
  <div class="item"><svg class="av" width="32" height="32"><use href="#user"/></svg><div><a class="t">Fahrradtour</a><p class="m">Paul · 20. April 2017</p></div></div>
  <div class="item"><svg class="av" width="32" height="32"><use href="#user"/></svg><div><a class="t">Biken mal anders</a><p class="m">Sara · 20. April 2017</p></div></div>
  <div class="item"><svg class="av" width="32" height="32"><use href="#user"/></svg><div><a class="t">Der Wettbewerb im nächsten Monat</a><p class="m">Tim · 18. April 2017</p></div></div>
</aside>

<aside class="abs side" style="left:793px;top:1292px;width:316px;height:166px">
  <div class="panel-head">ANSTEHENDE TERMINE</div>
  <div class="item"><i class="av blank"></i><div><a class="t">Fahrradtour in den Bergen</a><p class="m">Montag 01. Mai 2017</p></div></div>
  <div class="item"><i class="av photo"></i><div><a class="t">Workshop Extremes Biken</a><p class="m">Dienstag 29. Mai 2017</p></div></div>
</aside>

<a class="abs totop" aria-label="Nach oben"><svg width="28" height="18" viewBox="0 0 28 18"><path d="M3 15L14 4l11 11" stroke="#2a8be0" stroke-width="5" fill="none"/></svg></a>

<h2 class="abs section-title" style="top:1514px">UNSERE ZWEIRAD-COMMUNITY HAT VIEL ZU BIETEN</h2>
<div class="abs rule" style="left:532px;width:136px;top:1563px"></div>
<p class="abs lead" style="top:1580px">Schön das Sie uns gefunden haben. Legen Sie doch gleich los<br>und entdecken Sie unsere Zweirad-Communitys</p>

<div class="abs card" style="left:40px">
  <div class="img" role="img" aria-label="Foto: Radfahrer im Sonnenuntergang" style="background:linear-gradient(135deg,#e6b24a,#7a5a38 55%,#3d3a3a)"></div>
  <div class="arc"></div>
  <div class="brand" style="color:var(--green)"><i style="background:var(--green)"></i>Fahrrad.Treff</div>
  <a class="cta" style="background:var(--green)">ZUR COMMUNITY</a>
</div>
<div class="abs card" style="left:414px">
  <div class="img" role="img" aria-label="Foto: Motorradfahrer auf Landstraße" style="background:linear-gradient(135deg,#7f8a55,#4a4a44 50%,#9ca36a)"></div>
  <div class="arc"></div>
  <div class="brand" style="color:var(--red)"><i style="background:var(--red)"></i>Motorrad.Treff</div>
  <a class="cta" style="background:var(--red)">ZUR COMMUNITY</a>
</div>
<div class="abs card" style="left:788px;width:323px">
  <div class="img" role="img" aria-label="Foto: Rollerfahrerin auf der Straße" style="background:linear-gradient(135deg,#9a9a98,#5e5e60 50%,#c2c0bb)"></div>
  <div class="arc"></div>
  <div class="brand"><i></i>Roller.Treff</div>
  <a class="cta" style="background:var(--blue)">ZUR COMMUNITY</a>
</div>

<div class="abs map" role="img" aria-label="Karte der Mitglieder-Standorte mit Markierung"></div>

<footer class="abs footer">
  <div class="brand"><i></i>Roller.Treff</div>
  <p class="about">Lorem ipsum dolor sit amet, consetetur sa dipscing eirmod dolore magna aliquyam erat sed diam voluptua. Rrat sed diam voluptua. Lorem ipsum dolor sit amet, consetetur sa dipscing elitr.</p>
  <div class="fcol" style="left:413px"><h3>LINKS</h3><ul><li>DASHBOARD</li><li>FORUM</li><li>MITGLIEDER</li><li>MARKTPLATZ</li><li>GALERIE</li><li>KALENDER</li><li>NEWS</li></ul></div>
  <div class="fcol" style="left:667px"><h3>LETZTE BEITRÄGE</h3>
    <div class="fpost"><i></i><div>Neues Communitydesign<small>Anna · 27. April 2017</small></div></div>
    <div class="fpost"><i></i><div>Spannendes Thema<small>Paula · 27. April 2017</small></div></div>
    <div class="fpost"><i></i><div>Und noch ein anderes<small>Tim · 27. April 2017</small></div></div>
  </div>
  <div class="fcol nl" style="left:914px"><h3>NEWSLETTER</h3><input placeholder="Ihre Emailadresse"><div class="go">JETZT ANMELDEN</div></div>
</footer>
<div class="abs bottombar">© Roller.Treff - Impressum &amp; Kontakt | AGB</div>

</body>
</html>
```